Web Design Project

We are looking for a new site design for the VELTO Canada. The current site can be found at
http://www.veltocanada-example.org/
The URL is provided for reference. We want a completely different look and layout which is shown in the specifications document.
As part of the design, we want a home page, and inside page.
The design you provide will be implemented in Joomla. The design winner will only need to provide the PSD. We anticipate creating the template coding in-house.
However, if you have experience creating Joomla templates, please let us know as we may ask you to bid separately to do that phase of the project.
We've provided a specifications document which includes wireframes of the home page, and inside page. We've also included a logo file.
For the header at the top, as indicated in the specs document, we want to keep the same overall treatment to every page. We want a graphic treatment with the logo for the header area. In this manner, the design will be flexiable and can be used for future years.
For the home page, we've indicated that we'd like to have a slider implemented within the design.
The wireframe is provided to illustrate the placement of content and menu items. The exact dimensions of each component can be revised as you see fit. We are also flexiable if you feel we have missed items.

```html
<!DOCTYPE html>
<html lang="en">
<head>
<meta charset="utf-8">
<title>VELTO Canada – Home</title>
<link rel="stylesheet" href="https://fonts.googleapis.com/css2?family=Maven+Pro:wght@400;500;600;700&display=swap">
<style>
:root{
  --blue:#1d4a8f;
  --blue-dark:#163a72;
  --page:#f3f4f6;
  --panel:#e9e9ea;
  --ink:#2a2a2a;
  --muted:#6a6a6a;
  --dark:#222325;
  --news:#1f2125;
  --red:#d9191f;
  --yellow:#f7e70c;
  --link:#1f5ea8;
}
*{box-sizing:border-box;margin:0;padding:0}
html,body{width:974px;height:1200px;overflow:hidden;background:var(--page)}
body{font-family:"Maven Pro",sans-serif;color:var(--ink)}
.stage{position:absolute;left:0;top:0;width:1200px;height:1478px;transform:scale(.811667);transform-origin:0 0;background:var(--page)}
.abs{position:absolute}

.topbar{left:0;top:0;width:1200px;height:31px;background:var(--blue);color:#fff;font-size:11px}
.topbar .contact{position:absolute;left:142px;top:9px;display:flex;gap:16px;align-items:center}
.topbar .contact span{display:flex;gap:6px;align-items:center}
.topbar .links{position:absolute;right:142px;top:9px;display:flex;gap:30px}
.topbar .links .active{color:var(--yellow)}

.brand{left:152px;top:48px;display:flex;align-items:center;gap:12px}
.brand .mark{width:60px;height:60px;border-radius:50%;background:var(--blue)}
.brand .name{font-size:32px;font-weight:700;color:var(--blue);letter-spacing:1px}

.social{left:735px;top:94px;display:flex;gap:3px}
.social i{display:block;width:24px;height:24px;border-radius:50%}

.mainnav{left:122px;top:195px;width:960px;height:56px;background:linear-gradient(#fafafa,#e6e6e6);display:flex;font-size:13px;font-weight:500;box-shadow:0 6px 8px -6px rgba(0,0,0,.25)}
.mainnav .home{width:52px;background:var(--blue);display:flex;align-items:center;justify-content:center}
.mainnav a{display:flex;align-items:center;justify-content:center;border-right:1px solid #d6d6d6;color:var(--ink);text-decoration:none}
.mainnav a.current{color:var(--link)}

.slider{left:122px;top:288px;width:960px;height:396px;background:var(--dark);border-radius:6px;box-shadow:0 3px 6px rgba(0,0,0,.3)}
.slider .photo{position:absolute;left:18px;top:18px;width:922px;height:356px;background:radial-gradient(ellipse at 50% 45%,#e8963f 0%,#b65420 45%,#5d1c0c 100%)}
.slider .caption{position:absolute;left:283px;top:306px;width:385px;height:68px;background:rgba(40,20,10,.55);color:#fff;font-size:25px;line-height:30px;padding:4px 0 0 24px;white-space:nowrap}
.slider .caption b{color:var(--yellow);font-weight:600}
.slider .arrow{position:absolute;top:181px;width:36px;height:30px;background:#eee;border:2px solid #c22;border-radius:3px}
.slider .arrow::after{content:"";position:absolute;left:11px;top:8px;width:10px;height:10px;border-radius:50%;background:#888}
.slider .prev{left:-17px}
.slider .next{right:-13px}

.box{background:var(--panel)}
.box h3{font-size:14px;font-weight:600;letter-spacing:.5px;padding:12px 0 6px;margin:0 12px 0 16px;border-bottom:1px solid #c9c9c9}
.pill{display:block;background:#141414;color:#fff;border-radius:16px;text-align:center}

.sponsors{left:122px;top:713px;width:180px;height:185px}
.sponsors .logo{font-size:36px;font-weight:700;color:var(--blue);text-align:center;margin-top:32px}
.sponsors .pill{position:absolute;left:10px;top:143px;width:158px;height:32px;line-height:32px;font-size:13px}

.login{left:122px;top:913px;width:180px;height:185px}
.login .field{position:absolute;left:11px;width:158px;height:32px;border-radius:16px;background:#f6f6f6;border:1px solid #d5d5d5;font-size:11px;color:var(--muted);padding:9px 22px}
.login .remember{position:absolute;left:38px;top:124px;font-size:11px;color:var(--muted);display:flex;gap:10px;align-items:center}
.login .remember i{width:12px;height:12px;border:1px solid #aaa;background:#fff}
.login .pill{position:absolute;left:35px;top:150px;width:108px;height:24px;line-height:24px;font-size:12px;font-weight:600}

.feature{left:316px;top:713px;width:766px;height:385px}
.feature .photo{position:absolute;left:24px;top:22px;width:449px;height:141px;background:linear-gradient(180deg,#e9e3d4,#b49a7b 55%,#4b4742)}
.feature .lead{position:absolute;left:24px;top:173px;width:430px;font-size:12px;font-weight:600;line-height:22px}
.feature .body{position:absolute;left:24px;top:223px;width:445px;font-size:11px;line-height:21px}
.feature .more{position:absolute;left:24px;top:338px;width:87px;height:30px;background:#151515;color:#fff;font-size:10.5px;font-weight:700;line-height:30px;text-align:center}

.news{position:absolute;left:532px;top:22px;width:212px;height:342px;background:var(--news);color:#fff}
.news h3{font-size:14px;font-weight:600;padding:10px 12px 8px;margin:0 44px 0 0;border-bottom:1px solid #555}
.news .item{position:absolute;left:28px;width:160px}
.news .title{font-size:11px;font-style:italic;color:#b7b7b7;line-height:18px}
.news .title.hl{color:#4e9de5}
.news .text{font-size:10px;line-height:21px;margin-top:8px}
.news .rule{position:absolute;left:28px;top:184px;width:158px;border-top:1px solid #555}
.date{position:absolute;left:-73px;top:2px;width:65px;height:47px;color:#fff;font-size:13px;font-weight:700;text-align:center;line-height:15px;padding-top:8px}
.date.grey{background:#5c5c5c}
.date.blue{background:var(--blue)}
.pager{position:absolute;right:12px;bottom:10px;display:flex;gap:4px;font-size:10px;font-weight:600}
.pager span{width:18px;height:20px;line-height:20px;text-align:center}
.pager .on{background:var(--blue)}

.connected{left:122px;top:1114px;width:180px;height:184px}
.connected p{font-size:11px;line-height:21px;margin:10px 12px 0 15px}
.connected .icons{position:absolute;left:18px;top:103px;display:grid;grid-template-columns:repeat(4,30px);gap:8px 8px}
.connected .icons i{width:30px;height:30px;border-radius:50%;background:#595959}
.connected .icons i.on{background:#1e9bd8}
.connected .tip{position:absolute;left:40px;top:146px;width:62px;height:16px;border-radius:3px;background:#1e9bd8;color:#fff;font-size:9px;text-align:center;line-height:16px}

.regions{left:316px;top:1114px;width:766px;height:184px;overflow:hidden}
.regions h3{margin:0 0 0 18px;width:155px;padding:12px 0 6px 5px}
.regions .map{position:absolute;right:0;top:0;width:260px;height:184px;background:radial-gradient(circle at 40% 40%,#f0eded 0 30%,#d9dcde 60%,#c6c9cc 100%)}
.regions .cols{position:absolute;left:24px;top:58px;display:flex;font-size:11px;line-height:23.5px}
.regions .cols div{width:141px}
.regions .cols div:nth-child(2){width:107px}
.regions .cols div:nth-child(3){width:159px}
.regions .cols strong{display:block;font-size:12px;font-weight:600;margin-bottom:1px}
.regions .cols .hl{color:var(--link);padding-left:12px}

.follow{left:121px;top:1313px;width:961px;height:71px;background:linear-gradient(90deg,#c9141a,#e52227 60%,#d01a1f)}
.follow .dot{position:absolute;left:44px;top:6px;width:60px;height:60px;border-radius:50%;background:#fff}
.follow p{position:absolute;left:156px;top:8px;color:#fff;font-size:16px;font-weight:600;font-style:italic;line-height:27px}

.footnav{left:0;top:1400px;width:1200px;height:40px;background:var(--blue);color:#fff;font-size:11px;display:flex;justify-content:center;align-items:center;gap:10px}
.footnav .on{color:var(--yellow)}
.footbar{left:0;top:1440px;width:1200px;height:38px;background:#1f2021;color:#fff;font-size:11px;display:flex;justify-content:center;align-items:center;gap:12px}
</style>
</head>
<body>
<div class="stage">

  <header class="abs topbar">
    <div class="contact">
      <span><svg width="10" height="10" viewBox="0 0 10 10"><path d="M2 0l2 2-1 1.5c.8 1.5 2 2.7 3.5 3.5L8 6l2 2-1.5 2C4.5 9.5.5 5.5 0 1.5z" fill="#fff"/></svg>555-014-2290</span>
      <span>/</span>
      <span><svg width="11" height="8" viewBox="0 0 11 8"><rect width="11" height="8" fill="#fff"/><path d="M0 0l5.5 4.5L11 0" stroke="#1d4a8f" fill="none"/></svg>contact@veltocanada-example.org</span>
    </div>
    <nav class="links"><span class="active">Home</span><span>Contact Us</span><span>VELTO International</span></nav>
  </header>

  <div class="abs brand"><span class="mark"></span><span class="name">VELTO Canada</span></div>

  <div class="abs social" aria-label="Social links">
    <i style="background:#f7931e"></i><i style="background:#d0161f"></i><i style="background:#0e76a8"></i><i style="background:#1a5ea3"></i><i style="background:#ea4c89"></i><i style="background:#dd4b39"></i><i style="background:#2c4762"></i><i style="background:#1ab7ea"></i><i style="background:#c4302b"></i><i style="background:#e0117f"></i><i style="background:#1da1f2"></i><i style="background:#3b5998"></i>
  </div>

  <nav class="abs mainnav">
    <span class="home"><svg width="18" height="16" viewBox="0 0 18 16"><path d="M9 0l9 8h-3v8h-4v-5H7v5H3V8H0z" fill="#fff"/></svg></span>
    <a style="width:109px">About</a><a style="width:98px">Board</a><a class="current" style="width:115px">Chapters</a><a style="width:145px">Member Space</a><a style="width:200px">Resources &amp; Knowledge</a><a style="width:133px">Sponsorship</a><a style="width:108px;border:0">Exhibit</a>
  </nav>

  <section class="abs slider">
    <div class="photo" role="img" aria-label="Conference boardroom with long table and leather chairs"></div>
    <div class="caption">VELTO Canada Conference<br>Saskatoon.SK&nbsp; <b>June 2-5.2013</b></div>
    <span class="arrow prev"></span><span class="arrow next"></span>
  </section>

  <aside class="abs box sponsors">
    <h3>SPONSORS</h3>
    <div class="logo">Norvane</div>
    <a class="pill">Become a Sponsor</a>
  </aside>

  <aside class="abs box login">
    <h3>MEMBER LOGIN</h3>
    <span class="field" style="top:48px">Account login</span>
    <span class="field" style="top:86px">Password</span>
    <span class="remember"><i></i>Remember Me</span>
    <a class="pill">Login</a>
  </aside>

  <main class="abs box feature">
    <div class="photo" role="img" aria-label="Business team meeting around a table"></div>
    <p class="lead">Etiam ullamcorper. Suspendisse a pellentesque dui, non feliss porta urna. Vestibulum commodo volutpat a, convallis ac, laoreet enim.</p>
    <p class="body">Vestibulum commodo volutpat a, convallis ac, laoreet enim. erat ac ipsum. Integer aliquam purus. Quisque lorem tortor fringilla sed, vestibulum id, eleifend justo vel bibendum sapien massa ac turpis faucibus orci luctus non, consectetuer lobortis quis, varius in, purus. Vestibulum commodo volutpat a, convallis ac, laoreet enim. er lobortis quis, varius in, purus.</p>
    <a class="more">READ MORE</a>

    <section class="news">
      <h3>LATEST NEWS</h3>
      <div class="item" style="top:46px">
        <span class="date grey">05/01<br>2013</span>
        <p class="title">Mobile Marketing: Too Big an Opportunity for Companies to Ignore</p>
        <p class="text">Vestibulum commodo volutpat a, convallis ac, laoreet enim. erat ac ipsum. Integer aliquam purus.</p>
      </div>
      <span class="rule"></span>
      <div class="item" style="top:200px">
        <span class="date blue">14/12<br>2012</span>
        <p class="title hl">Using Social Media to Land the Right Candidate</p>
        <p class="text">Vestibulum commodo volutpat a, convallis ac, laoreet enim. erat ac ipsum. Integer aliquam purus.</p>
      </div>
      <div class="pager"><span class="on">1</span><span>2</span><span>&#9654;</span></div>
    </section>
  </main>

  <aside class="abs box connected">
    <h3>STAY CONNECTED</h3>
    <p>Vestibulum commodo volutpat a, convallis ac, laoreet.</p>
    <div class="icons"><i></i><i class="on"></i><i></i><i></i><i></i><i></i><i></i></div>
    <span class="tip">Follow</span>
  </aside>

  <section class="abs box regions">
    <h3>REGIONS</h3>
    <div class="map" role="img" aria-label="World map under a magnifying glass highlighting Canada"></div>
    <div class="cols">
      <div><strong>Mountain Pacific</strong>Vancouver Island<br>Vancouver<br>Calgary</div>
      <div><strong>Western</strong>Edmonton<br><span class="hl">Saskatchewan</span><br>Winnipeg</div>
      <div><strong>Central</strong>National Capital-Ottawa<br>Southwestern Ontario<br>Montreal<br>Toronto</div>
      <div><strong>Atlantic</strong>Nova Scotia<br>Terra Nova-St. John's<br>Prince Edward Island<br>Atlantic-St.John</div>
    </div>
  </section>

  <section class="abs follow">
    <span class="dot"></span>
    <p>OF COURSE, DON'T FORGET TO FOLLOW US AT<br>@veltocanada.com</p>
  </section>

  <nav class="abs footnav">
    <span class="on">Home</span>•<span>About</span>•<span>Board</span>•<span>Chapters</span>•<span>Member Space</span>•<span>Resources &amp; Knowledge</span>•<span>Sponsorship</span>•<span>Exhibit</span>•<span>Member Login</span>•<span>Contact Us</span>
  </nav>
  <footer class="abs footbar">
    <span>Privacy Policy</span>•<span>Terms Of Use</span>•<span>Privacy Statement © Copyright 2013 by VELTO Canada International</span>
  </footer>

</div>
</body>
</html>
```